Packaging Design Project For Chocolate Brand

We need a fresh, vibrant and colourful packaging for our healthy chocolate brand, oTakeFernubrio.

WHAT IS oTakeFernubrio?

oTakeFernubrio are indulgent chocolates that help reduce your body weight by controlling your appetite and calorie intake. And the best thing is that it tastes 100% genuine chocolate, only healthier.

WHAT WE NEED FROM YOU

Although we have collected a few logos from other designers, it's not quite catchy to the eye. As it will appear on retail shelves, it needs to catch the eye. It's up to the designers if they want to design the logo all in one word or two words. We will provide feedback quickly. We are contemplating on a sub-title beneath the logo, with the words "Unwrap. Eat. Lose." It is the main logo "oTakeFernubrio" that needs to stand out though with possibly some chocolatey or slimming/dieting aspect. However we do not want any images of thin bodies around the logo. Use of imagination involving chocolate could be beneficial, e.g. melting chocolate etc.
Use different colours for 'i', 'Love', and 'Fernubrio'. Maybe include an illustration around the logo if you feel it will brighten the brand.

Packaging

Although we do not have a specific theme in mind, the designer may want to try a retro look with illustrations/images, funky, maybe professional but keep it modern and looking like a chocolate bar.

Dimensions - 155mm(width) x 76.8mm(height) x 34mm(depth)
Portrait or landscape. Designers choice.

There are three flavours, Milk, White and Dark so three different packages with different colours. The rest of the packages will look more or less the same. The packaging itself needs 'wavey' aspects of chocolate. Wavey, circular, elegant shapes which appeal to the eye

There are certain texts which need to go on the front end of the box. The designer has the option of using 2 different texts in their work to come up with the best design. Texts are on the files. More text may be added but in the meantime please use what is given.
Updates

Project Deadline Extended
Reason: Hi, The deadline has been extended a further 7 days for those who designers who started their designs late are concerned about the timeframe. So there is no need to rush your designs. I hope the 7 days extension is enough for those that need it. Many thanks,

Target Market(s)

Women aged 16-45, C1C2 class

Industry/Entity Type

Landscape

Requirements
Must have
• Appealing mostly to women aged 16-45, C1C2 class.
Colourful
Chocolatey feel with wavey lines etc
Strong Logo
Nice to have
• It can come across as a food supplement that you normally see on the pharmacy shelf but with an unconventional design twist. Or the designer may think it will not work and for it to have the chocolatey feel, there cannot be any connection a pharmaceutical package. It has to remain like a regular chocolate bar that you see in the supermarket. Up to the designer to choose. It will be going into both supermarket stores and healthfood stores.

The designer should have some personal input in the design. If you were browsing around the supermarket and spotted it, would you stop and look at it? If not, the design will need changing.

Secondly, maybe a brand illustration would go well with the logo. Possibly an animal illustration relating to chocolate (somehow) or simply a chocolate with a measuring tape around it getting slimmer and slimmer. Just a few thoughts

```html
<!DOCTYPE html>
<html lang="en">
<head>
<meta charset="utf-8">
<title>oTakeFernubrio Dark – Pack Front</title>
<link rel="stylesheet" href="https://fonts.googleapis.com/css2?family=Sofia&family=Advent+Pro:wght@400;500&family=Bungee&family=Bungee+Outline&display=swap">
<style>
  :root {
    --pack-orange: #ff6a00;
    --panel-black: #0a0409;
    --claim-red: #880000;
    --badge-cream: #ffffcc;
    --badge-red: #d10f0f;
    --badge-red-deep: #5a0808;
    --ink: #000000;
    --white: #ffffff;
  }
  * { margin: 0; padding: 0; box-sizing: border-box; }
  html, body {
    width: 1200px;
    height: 602px;
    overflow: hidden;
    background: var(--pack-orange);
  }
  .pack-front {
    position: relative;
    width: 1200px;
    height: 602px;
    background: var(--pack-orange);
  }
  .front-panel {
    position: absolute;
    left: 10px;
    top: 10px;
    width: 1180px;
    height: 515px;
    background: var(--panel-black);
    overflow: hidden;
  }
  .brand-name {
    position: absolute;
    left: 45px;
    top: 52px;
    font-family: "Sofia", cursive;
    font-weight: 400;
    font-size: 128px;
    line-height: 1.2;
    color: var(--white);
    white-space: nowrap;
  }
  .chocolate-swirl {
    position: absolute;
    left: 37px;
    top: 268px;
    width: 600px;
    height: 220px;
    border-radius: 50%;
    background: radial-gradient(ellipse at 48% 42%,
      rgba(90, 40, 42, 0.85) 0%,
      rgba(60, 26, 30, 0.7) 35%,
      rgba(40, 18, 22, 0.45) 65%,
      rgba(10, 4, 9, 0) 100%);
  }
  .flavour-badge {
    position: absolute;
    left: 946px;
    top: 46px;
    width: 175px;
    height: 186px;
    background: var(--badge-cream);
    border: 2px dashed var(--pack-orange);
  }
  .flavour-badge__art {
    position: absolute;
    left: 36px;
    top: 14px;
    width: 103px;
    height: 100px;
    border-radius: 40% 40% 50% 50%;
    background: radial-gradient(circle at 40% 45%, #ff2020 0%, var(--badge-red) 50%, var(--badge-red-deep) 100%);
  }
  .flavour-badge__name {
    position: absolute;
    left: 0;
    right: 0;
    top: 132px;
    text-align: center;
    font-family: "Bungee", sans-serif;
    font-size: 24px;
    line-height: 1;
    color: var(--badge-red);
    letter-spacing: 1px;
  }
  .claim-box {
    position: absolute;
    left: 644px;
    top: 279px;
    width: 475px;
    height: 184px;
    background: var(--claim-red);
    padding: 12px 13px 0 0;
    text-align: right;
    font-family: "Advent Pro", sans-serif;
    font-weight: 500;
    font-size: 30px;
    line-height: 32.5px;
    letter-spacing: 1.6px;
    word-spacing: 4px;
    text-transform: uppercase;
    color: var(--white);
  }
  .claim-box__line {
    display: block;
    white-space: nowrap;
  }
  .tagline {
    position: absolute;
    left: 0;
    right: 0;
    top: 534px;
    text-align: center;
    font-family: "Bungee Outline", sans-serif;
    font-size: 38px;
    line-height: 60px;
    letter-spacing: 3px;
    color: var(--ink);
    text-transform: uppercase;
    white-space: nowrap;
  }
</style>
</head>
<body>
  <main class="pack-front">
    <section class="front-panel">
      <h1 class="brand-name">oTakeFernubrio</h1>

      <div class="chocolate-swirl" role="img" aria-label="Swirl of melted dark chocolate with small coloured stars"></div>

      <div class="flavour-badge">
        <div class="flavour-badge__art" role="img" aria-label="Red heart dipped in melting dark chocolate"></div>
        <p class="flavour-badge__name">DARK</p>
      </div>

      <p class="claim-box">
        <span class="claim-box__line">This chocolate will fix more</span>
        <span class="claim-box__line">than just your cravings.</span>
        <span class="claim-box__line">This correctly proportioned</span>
        <span class="claim-box__line">amount eaten daily is proven</span>
        <span class="claim-box__line">to reduce body weight.</span>
      </p>
    </section>

    <p class="tagline">Unwrap. Eat. Lose.</p>
  </main>
</body>
</html>
```